KL Taxidermy

I need business Cards with my logo and a background photo of one of my taxidermy mounts.
I would like a black back drop behind it all and what ever looks best for my contact information (red or white?)
Garrick Pembley
592-718-4409
kltaxidermy482@mailnook.example
Chatterloom page

```html
<!DOCTYPE html>
<html lang="en">
<head>
<meta charset="utf-8">
<title>KL Taxidermy — Business Card</title>
<link rel="stylesheet" href="https://fonts.googleapis.com/css2?family=Open+Sans:wght@400;700&display=swap">
<style>
  :root {
    --backdrop: #0d0d0f;
    --photo-top: #dfe6ee;
    --photo-mid: #c3ccd6;
    --photo-low: #9aa6b3;
    --accent-red: #e0382d;
    --ink: #26272b;
    --brand-ink: #141416;
    --band-black: #121214;
    --band-silver: #c9ccd1;
    --band-red: #a3201b;
  }
  html, body {
    margin: 0;
    width: 1200px;
    height: 900px;
    overflow: hidden;
    background: var(--backdrop);
    font-family: "Open Sans", sans-serif;
  }
  .card {
    position: absolute;
    left: 100px;
    top: 164px;
    width: 1000px;
    height: 572px;
    overflow: hidden;
    box-shadow: 0 14px 40px rgba(0,0,0,0.5);
  }
  .mount-photo {
    position: absolute;
    inset: 0;
    background:
      radial-gradient(ellipse 260px 380px at 420px 260px, rgba(255,255,255,0.55), rgba(255,255,255,0) 70%),
      linear-gradient(180deg, var(--photo-top) 0%, var(--photo-mid) 55%, var(--photo-low) 100%);
  }
  .holder-name {
    position: absolute;
    left: 64px;
    top: 98px;
    margin: 0;
    font-size: 36px;
    line-height: 48px;
    font-weight: 700;
    color: var(--accent-red);
    letter-spacing: 0.3px;
  }
  .contact-list {
    position: absolute;
    left: 62px;
    top: 248px;
    margin: 0;
    padding: 0;
    list-style: none;
  }
  .contact-item {
    display: flex;
    align-items: center;
    gap: 18px;
    height: 38px;
    font-size: 27px;
    color: var(--ink);
  }
  .contact-icon {
    width: 28px;
    height: 28px;
    fill: var(--accent-red);
    flex-shrink: 0;
  }
  .brand-name {
    position: absolute;
    left: 600px;
    top: 160px;
    width: 370px;
    margin: 0;
    text-align: center;
    font-size: 42px;
    line-height: 58px;
    font-weight: 700;
    color: var(--brand-ink);
    letter-spacing: 1px;
  }
  .bottom-wave {
    position: absolute;
    left: 0;
    top: 0;
    width: 1000px;
    height: 572px;
  }
</style>
</head>
<body>
  <section class="card">
    <div class="mount-photo" role="img" aria-label="Photo of a taxidermy mount used as the card background"></div>

    <svg class="bottom-wave" viewBox="0 0 1000 572" aria-hidden="true">
      <path d="M0,436 Q300,470 520,505 Q760,532 1000,500 L1000,572 L0,572 Z" fill="var(--band-black)"/>
      <path d="M170,492 Q600,540 1000,470 L1000,500 Q760,532 520,505 Q330,478 170,492 Z" fill="var(--band-silver)"/>
      <path d="M170,490 Q600,522 1000,452 L1000,472 Q600,538 170,492 Z" fill="var(--band-red)"/>
    </svg>

    <h1 class="holder-name">GARRICK PEMBLEY</h1>

    <ul class="contact-list">
      <li class="contact-item">
        <svg class="contact-icon" viewBox="0 0 24 24" aria-hidden="true">
          <path d="M6.6 10.8a15.1 15.1 0 0 0 6.6 6.6l2.2-2.2a1 1 0 0 1 1-.25 11.4 11.4 0 0 0 3.6.57 1 1 0 0 1 1 1V20a1 1 0 0 1-1 1A17 17 0 0 1 3 4a1 1 0 0 1 1-1h3.5a1 1 0 0 1 1 1c0 1.25.2 2.45.57 3.57a1 1 0 0 1-.25 1z"/>
        </svg>
        <span>592-718-4409</span>
      </li>
      <li class="contact-item">
        <svg class="contact-icon" viewBox="0 0 24 24" aria-hidden="true">
          <path d="M2 5h20v14H2z" fill="var(--accent-red)"/>
          <path d="M3.5 6.5 12 13l8.5-6.5" fill="none" stroke="var(--photo-top)" stroke-width="1.4"/>
        </svg>
        <span>kltaxidermy482@mailnook.example</span>
      </li>
    </ul>

    <p class="brand-name">KL TAXIDERMY</p>
  </section>
</body>
</html>
```